Bref créative
business stationary package for dex9firm
envelopes, business cards, 2xcover sheets,ppt template, letterhead, mousepad, cd
Professional
Tobias Wendt
Lindmoosweg 7c
A-1230 Wien
tobias.wendt@dex9firm-example.at
www.dex9firm-example.at
We would need the following templates:
1) letterhead in the size A4
2) ppt presentation in the size A4 landscape
3) business cards in the size of 3.47x2.25in (88,22x57,22mm)
4) single page cover sheet for encrypted emails (A4 portrait)
5) cover sheet for handouts (A4 portrait)
6) mouse pad
7) cd cover sheet+cd design
8) envelope
dex9firm logo
mind: usage without the mirroring effect
demo encrypted message coversheet - ours should look similar but in the dex9firm design - having the same content - we should be able to edit the text
demo for other coversheet - a free rectangle area (cut out) should be placed similar to this upload. We want to print the title on the following page and it should be visible through this cover sheet.

```html
<!DOCTYPE html>
<html lang="de">
<head>
<meta charset="utf-8">
<title>dex9firm Geschäftsausstattung</title>
<link rel="stylesheet" href="https://fonts.googleapis.com/css2?family=Open+Sans:wght@400;600;700&display=swap">
<style>
  :root {
    --bg: #efefef;
    --paper: #ffffff;
    --brand: #1c5fa6;
    --brand-dark: #0f3f7a;
    --brand-light: #3b82c8;
    --ink: #4a4a4a;
    --muted: #9a9a9a;
    --band-silver: #e9edf2;
    --line: #dcdcdc;
  }
  * { box-sizing: border-box; margin: 0; padding: 0; }
  html, body { width: 1200px; height: 936px; overflow: hidden; }
  body {
    background: var(--bg);
    font-family: "Open Sans", Arial, sans-serif;
    color: var(--ink);
    position: relative;
  }
  .sheet { position: absolute; background: var(--paper); box-shadow: 0 2px 8px rgba(0,0,0,.12); overflow: hidden; }
  .wordmark { font-weight: 700; color: var(--brand); letter-spacing: -0.5px; line-height: 1; white-space: nowrap; }

  /* Letterhead */
  .letterhead { left: 178px; top: 38px; width: 385px; height: 557px; padding: 28px 34px; }
  .letterhead .wordmark { font-size: 26px; }
  .letter-body { margin-top: 182px; font-size: 5.5px; line-height: 1.6; }
  .letter-body p { margin-bottom: 8px; }
  .letter-body .recipient { margin-bottom: 10px; }
  .letter-body .recipient strong { font-weight: 700; }
  .letter-body .signature-space { height: 20px; border-bottom: 0.5px solid #bbb; width: 40px; margin-bottom: 3px; }
  .letter-footer {
    position: absolute; left: 0; right: 0; bottom: 8px; height: 14px;
    background: linear-gradient(90deg, var(--brand-dark), var(--brand-light));
    display: flex; align-items: center; justify-content: center; gap: 14px;
    font-size: 4.5px; color: #fff; white-space: nowrap;
  }

  /* Folder */
  .folder {
    left: 630px; top: 38px; width: 378px; height: 566px;
    background: radial-gradient(ellipse at 55% 42%, var(--brand-light) 0%, var(--brand) 45%, var(--brand-dark) 100%);
  }
  .folder-band {
    position: absolute; left: 0; right: 0; top: 224px; height: 100px;
    background: linear-gradient(180deg, #fff 0%, var(--band-silver) 100%);
    box-shadow: 0 2px 0 #c8d2dd, 0 -2px 0 #c8d2dd;
    display: flex; align-items: center; justify-content: center;
  }
  .folder-band .wordmark { font-size: 44px; }
  .folder-url {
    position: absolute; right: 32px; bottom: 26px;
    font-size: 21px; font-weight: 600; color: #fff; letter-spacing: 1px; white-space: nowrap;
  }

  /* Business cards */
  .card { left: 38px; width: 134px; height: 80px; }
  .card-back { top: 663px; padding: 8px 10px; }
  .card-back .wordmark { font-size: 16px; }
  .card-back .strip {
    position: absolute; left: 0; right: 0; bottom: 0; height: 38px;
    background: linear-gradient(90deg, var(--brand-dark), var(--brand-light));
    color: #fff; font-size: 4px; line-height: 1.6; padding: 6px 10px; white-space: nowrap;
  }
  .card-front {
    top: 776px; height: 96px;
    background: linear-gradient(120deg, var(--brand-light), var(--brand-dark));
    padding: 16px 10px;
  }
  .card-front .wordmark { color: #fff; font-size: 18px; }
  .card-front .card-url { position: absolute; left: 10px; bottom: 9px; font-size: 5.5px; color: #fff; white-space: nowrap; }

  /* Envelopes */
  .envelope-front { left: 228px; top: 663px; width: 404px; height: 210px; padding: 30px 38px; }
  .envelope-front .wordmark { font-size: 22px; }
  .envelope-front .sender { margin-top: 8px; font-size: 5.5px; color: var(--muted); }
  .envelope-back { left: 736px; top: 670px; width: 428px; height: 203px; }
  .envelope-back svg { position: absolute; left: 0; top: 0; }
  .envelope-back .wordmark { position: absolute; left: 0; right: 0; top: 34px; text-align: center; font-size: 19px; }
</style>
</head>
<body>

  <section class="sheet letterhead">
    <div class="wordmark">dex9firm</div>
    <div class="letter-body">
      <p>12. März 2024</p>
      <p class="recipient"><strong>Anna Berger</strong><br>Ringstraße 14, 1010 Wien</p>
      <p>Wir danken Ihnen für Ihr Vertrauen und senden Ihnen anbei die vereinbarten Unterlagen zur weiteren Prüfung. Die Dokumente enthalten alle besprochenen Punkte sowie eine Übersicht der nächsten Schritte. Bei Rückfragen stehen wir Ihnen jederzeit gerne zur Verfügung und freuen uns auf die weitere Zusammenarbeit mit Ihrem Team.</p>
      <p>Gerne vereinbaren wir einen Termin, um die Details gemeinsam durchzugehen und offene Fragen zu klären. Teilen Sie uns bitte mit, welcher Zeitraum Ihnen passt.</p>
      <p>Wir danken Ihnen für Ihr Vertrauen und senden Ihnen anbei die vereinbarten Unterlagen zur weiteren Prüfung. Die Dokumente enthalten alle besprochenen Punkte sowie eine Übersicht der nächsten Schritte. Bei Rückfragen stehen wir Ihnen jederzeit gerne zur Verfügung.</p>
      <p>Mit freundlichen Grüßen</p>
      <div class="signature-space"></div>
      <p>Tobias Wendt<br>Partner<br>Lindmoosweg 7c, A-1230 Wien</p>
    </div>
    <footer class="letter-footer">
      <span>Lindmoosweg 7c, A-1230 Wien</span>
      <span>+43 1 555 0142</span>
      <span>tobias.wendt@dex9firm-example.at</span>
      <span>www.dex9firm-example.at</span>
    </footer>
  </section>

  <section class="sheet folder">
    <div class="folder-band"><span class="wordmark">dex9firm</span></div>
    <div class="folder-url">www.dex9firm-example.at</div>
  </section>

  <section class="sheet card card-back">
    <div class="wordmark">dex9firm</div>
    <div class="strip">Tobias Wendt · Partner<br>Lindmoosweg 7c, A-1230 Wien<br>tobias.wendt@dex9firm-example.at</div>
  </section>

  <section class="sheet card card-front">
    <div class="wordmark">dex9firm</div>
    <div class="card-url">www.dex9firm-example.at</div>
  </section>

  <section class="sheet envelope-front">
    <div class="wordmark">dex9firm</div>
    <div class="sender">Lindmoosweg 7c · A-1230 Wien</div>
  </section>

  <section class="sheet envelope-back">
    <svg width="428" height="203" viewBox="0 0 428 203" aria-hidden="true">
      <polyline points="0,0 214,80 428,0" fill="none" stroke="var(--line)" stroke-width="1"/>
    </svg>
    <div class="wordmark">dex9firm</div>
  </section>

</body>
</html>
```